BHG Letterhead

I need letterhead for "birch hollow gateway llc" ...

logo attached to project..

Company Info:
482 South Marigold Avenue, Suite 7D
Chicago, Illinois 60617
ofc 312-555-0148
facsimile 312-555-0193
www.birchhollowgatewayllc.example
info@birchhollowgatewayllc.example

I have multiple projects listed.. see below:

Business cards for birch hollow gateway llc
letterhead "
envelopes "

Business cards for KP Vending LLC
letterhead "
envelopes "

Industry/Entity Type

It Company

```html
<!DOCTYPE html>
<html lang="en">
<head>
<meta charset="utf-8">
<title>BHG Letterhead</title>
<link rel="stylesheet" href="https://fonts.googleapis.com/css2?family=Crimson+Text:ital,wght@0,400;1,600&display=swap">
<style>
  :root {
    --paper: #ffffff;
    --brand-navy: #1f3f74;
    --text-navy: #1c3a6b;
    --mist: #eef1f6;
    --mist-fade: rgba(238, 241, 246, 0);
  }
  * { margin: 0; padding: 0; box-sizing: border-box; }
  html, body {
    width: 848px;
    height: 1200px;
    overflow: hidden;
    background: var(--paper);
  }
  .letterhead {
    position: relative;
    width: 848px;
    height: 1200px;
    background: var(--paper);
    font-family: "Crimson Text", Georgia, serif;
  }
  .backdrop-mark {
    position: absolute;
    left: 95px;
    top: 340px;
    width: 660px;
    height: 480px;
    border-radius: 40px;
    background: radial-gradient(ellipse at 50% 45%, var(--mist) 0%, var(--mist) 40%, var(--mist-fade) 72%);
  }
  .brand {
    position: absolute;
    left: 36px;
    top: 1050px;
    display: flex;
    align-items: center;
    gap: 10px;
  }
  .brand-square {
    width: 12px;
    height: 12px;
    background: var(--brand-navy);
  }
  .brand-name {
    font-weight: 400;
    font-size: 24px;
    letter-spacing: 0.5px;
    font-variant: small-caps;
    color: var(--brand-navy);
    line-height: 1;
    white-space: nowrap;
  }
  .contact {
    position: absolute;
    left: 36px;
    top: 1102px;
    font-style: italic;
    font-weight: 600;
    font-size: 12.5px;
    line-height: 17.5px;
    color: var(--text-navy);
    white-space: nowrap;
  }
  .contact .label { font-weight: 600; }
  .contact .sep { padding: 0 7px; }
</style>
</head>
<body>
  <main class="letterhead">
    <div class="backdrop-mark" role="img" aria-label="Faint brand emblem watermark area"></div>

    <div class="brand">
      <span class="brand-square" aria-hidden="true"></span>
      <span class="brand-name">Birch Hollow Gateway llc</span>
    </div>

    <address class="contact">
      <div class="contact-line">482 South Marigold Avenue, Suite 7D, Chicago, Illinois 60617</div>
      <div class="contact-line"><span class="label">ofc</span> 312-555-0148<span class="sep">|</span><span class="label">facsimile</span> 312-555-0193</div>
      <div class="contact-line"><span class="label">url</span> www.birchhollowgatewayllc.example<span class="sep">|</span><span class="label">email</span> info@birchhollowgatewayllc.example</div>
    </address>
  </main>
</body>
</html>
```